President
General Contractor
I need single sided standard sized Business Card [3.5" x 2"]
I am open to ideas
Simple
Darnell Whitby
President/CEO
P.O. Box 7413
Cedarvale, SC 29990
darnell@keystrelbuilderssc.example
www.keystrelbuilderssc.example
K573841 and R408657
Designers, you may want to check out my website. wwwkeystrelbuilderssc.example I have a log that Iam not crazy about. I want it to reflect more about residential and commerical construction, development and construction management.
I am open to using the back of the card.
Company's Logo

```html
<!DOCTYPE html>
<html lang="en">
<head>
<meta charset="utf-8">
<title>Keystrel Builders — Stationery Set</title>
<link rel="stylesheet" href="https://fonts.googleapis.com/css2?family=Montserrat:wght@400;600;800&display=swap">
<style>
  :root {
    --bg: #333333;
    --paper: #ffffff;
    --brand-red: #8a1114;
    --brand-red-light: #b07c7d;
    --mark-faint: #eee8e8;
    --ink: #555555;
    --caption: #8f8f8f;
    --fold: #d8d8d8;
  }
  * { box-sizing: border-box; margin: 0; padding: 0; }
  html, body { width: 1200px; height: 349px; overflow: hidden; }
  body {
    background: var(--bg);
    font-family: "Montserrat", Arial, sans-serif;
    position: relative;
  }
  .piece { position: absolute; filter: drop-shadow(0 2px 3px rgba(0,0,0,.45)); }
  .piece svg { display: block; }
  .caption {
    position: absolute;
    font-size: 6px;
    color: var(--caption);
    text-align: center;
  }
  .brand-block { position: absolute; left: 12px; top: 12px; }
  .brand-square { width: 40px; height: 40px; background: var(--brand-red); }
  .brand-name {
    margin-top: 30px;
    color: var(--paper);
    font-weight: 800;
    font-size: 17px;
    line-height: 18px;
    letter-spacing: .3px;
  }
  .brand-tag { margin-top: 4px; font-size: 6px; color: var(--caption); }
</style>
</head>
<body>

<!-- Brand heading -->
<div class="brand-block">
  <div class="brand-square"></div>
  <div class="brand-name">KEYSTREL<br>BUILDERS</div>
  <div class="brand-tag">Stationery set</div>
</div>

<!-- Business card -->
<div class="piece" style="left:12px;top:138px;">
  <svg width="108" height="60" viewBox="0 0 108 60" font-family="Montserrat, Arial, sans-serif">
    <rect width="108" height="60" fill="var(--paper)"/>
    <path d="M0 0 H30 C24 20 28 40 44 60 H0 Z" fill="var(--brand-red)"/>
    <rect x="6" y="7" width="9" height="9" fill="var(--paper)"/>
    <text x="6" y="23" font-size="4.2" font-weight="800" fill="var(--paper)">KEYSTREL</text>
    <text x="6" y="28" font-size="4.2" font-weight="800" fill="var(--paper)">BUILDERS</text>
    <text x="56" y="15" font-size="3.6" font-weight="600" fill="var(--brand-red)">Darnell Whitby</text>
    <text x="56" y="19.5" font-size="2.4" fill="var(--ink)">President/CEO</text>
    <text x="56" y="28" font-size="2.2" fill="var(--ink)">P.O. Box 7413</text>
    <text x="56" y="31.5" font-size="2.2" fill="var(--ink)">Cedarvale, SC 29990</text>
    <text x="56" y="37" font-size="1.9" fill="var(--ink)">darnell@keystrelbuilderssc.example</text>
    <text x="56" y="40.5" font-size="1.9" fill="var(--ink)">www.keystrelbuilderssc.example</text>
    <text x="56" y="46" font-size="1.9" fill="var(--ink)">Licensed and insured</text>
  </svg>
</div>
<div class="caption" style="left:12px;top:207px;width:108px;">Business Card</div>

<!-- Letterhead, logo left -->
<div class="piece" style="left:161px;top:19px;">
  <svg width="228" height="293" viewBox="0 0 228 293" font-family="Montserrat, Arial, sans-serif">
    <rect width="228" height="293" fill="var(--paper)"/>
    <rect x="22" y="8" width="14" height="11" fill="var(--brand-red)"/>
    <text x="16" y="25" font-size="4.4" font-weight="800" fill="var(--brand-red)">KEYSTREL</text>
    <text x="16" y="30" font-size="4.4" font-weight="800" fill="var(--brand-red)">BUILDERS</text>
    <g font-size="2.2" fill="var(--ink)">
      <text x="164" y="10">P.O. Box 7413</text>
      <text x="164" y="13.5">Cedarvale, SC 29990</text>
      <text x="164" y="17">darnell@keystrelbuilderssc.example</text>
      <text x="164" y="20.5">www.keystrelbuilderssc.example</text>
    </g>
    <rect x="80" y="108" width="70" height="70" fill="var(--mark-faint)"/>
    <path d="M0 262 C80 274 170 268 228 248 V253 C170 272 80 279 0 266 Z" fill="var(--brand-red-light)"/>
    <path d="M0 268 C80 281 170 274 228 255 V293 H0 Z" fill="var(--brand-red)"/>
    <text x="114" y="288" font-size="2.2" fill="var(--paper)" text-anchor="middle">Residential and commercial construction · www.keystrelbuilderssc.example</text>
  </svg>
</div>
<div class="caption" style="left:161px;top:318px;width:228px;">Letterhead</div>

<!-- Letterhead, logo centred -->
<div class="piece" style="left:401px;top:19px;">
  <svg width="228" height="293" viewBox="0 0 228 293" font-family="Montserrat, Arial, sans-serif">
    <rect width="228" height="293" fill="var(--paper)"/>
    <rect x="107" y="8" width="14" height="11" fill="var(--brand-red)"/>
    <text x="114" y="25" font-size="4.4" font-weight="800" fill="var(--brand-red)" text-anchor="middle">KEYSTREL BUILDERS</text>
    <rect x="80" y="108" width="70" height="70" fill="var(--mark-faint)"/>
    <path d="M0 262 C80 274 170 268 228 248 V253 C170 272 80 279 0 266 Z" fill="var(--brand-red-light)"/>
    <path d="M0 268 C80 281 170 274 228 255 V293 H0 Z" fill="var(--brand-red)"/>
    <text x="114" y="288" font-size="2.2" fill="var(--paper)" text-anchor="middle">P.O. Box 7413 · Cedarvale, SC 29990 · darnell@keystrelbuilderssc.example</text>
  </svg>
</div>
<div class="caption" style="left:401px;top:318px;width:228px;">Letterhead</div>

<!-- Envelope fronts -->
<div class="piece" style="left:637px;top:66px;">
  <svg width="256" height="114" viewBox="0 0 256 114" font-family="Montserrat, Arial, sans-serif">
    <rect width="256" height="114" fill="var(--paper)"/>
    <rect x="12" y="8" width="11" height="9" fill="var(--brand-red)"/>
    <text x="8" y="23" font-size="3.8" font-weight="800" fill="var(--brand-red)">KEYSTREL</text>
    <text x="8" y="27.5" font-size="3.8" font-weight="800" fill="var(--brand-red)">BUILDERS</text>
    <rect x="150" y="26" width="50" height="50" fill="var(--mark-faint)"/>
    <path d="M0 100 C80 110 180 104 256 86 V90 C180 108 80 113 0 103 Z" fill="var(--brand-red-light)"/>
    <path d="M0 104 C80 114 180 108 256 92 V114 H0 Z" fill="var(--brand-red)"/>
  </svg>
</div>
<div class="caption" style="left:637px;top:186px;width:256px;">Envelope</div>

<div class="piece" style="left:637px;top:204px;">
  <svg width="256" height="114" viewBox="0 0 256 114" font-family="Montserrat, Arial, sans-serif">
    <rect width="256" height="114" fill="var(--paper)"/>
    <rect x="12" y="8" width="11" height="9" fill="var(--brand-red)"/>
    <text x="8" y="23" font-size="3.8" font-weight="800" fill="var(--brand-red)">KEYSTREL</text>
    <text x="8" y="27.5" font-size="3.8" font-weight="800" fill="var(--brand-red)">BUILDERS</text>
    <rect x="150" y="26" width="50" height="50" fill="var(--mark-faint)"/>
    <path d="M0 100 C80 110 180 104 256 86 V90 C180 108 80 113 0 103 Z" fill="var(--brand-red-light)"/>
    <path d="M0 104 C80 114 180 108 256 92 V114 H0 Z" fill="var(--brand-red)"/>
  </svg>
</div>
<div class="caption" style="left:637px;top:322px;width:256px;">Envelope</div>

<!-- Envelope stack -->
<div class="piece" style="left:908px;top:72px;">
  <svg width="280" height="246" viewBox="0 0 280 246" font-family="Montserrat, Arial, sans-serif">
    <!-- back with red flap -->
    <rect x="0" y="0" width="280" height="104" fill="var(--paper)"/>
    <path d="M0 0 H280 V10 L140 40 L0 10 Z" fill="var(--brand-red)"/>
    <rect x="135" y="18" width="10" height="8" fill="var(--paper)"/>
    <!-- back, plain -->
    <g transform="translate(0,52)">
      <rect width="280" height="96" fill="var(--paper)"/>
      <path d="M0 0 L140 40 L280 0" fill="none" stroke="var(--fold)" stroke-width="1"/>
      <path d="M0 96 L115 52 M280 96 L165 52" stroke="var(--fold)" stroke-width="1"/>
    </g>
    <!-- front -->
    <g transform="translate(0,130)">
      <rect width="280" height="116" fill="var(--paper)"/>
      <rect x="112" y="30" width="9" height="7" fill="var(--brand-red)"/>
      <text x="124" y="36" font-size="3.6" font-weight="800" fill="var(--brand-red)">KEYSTREL BUILDERS</text>
    </g>
  </svg>
</div>
<div class="caption" style="left:908px;top:322px;width:280px;">Envelope</div>

</body>
</html>
```